International Wine Label 202001

Need a wine label designed for several new wines from California being exported to Asia. This label should be focused around an animal theme of the flowing: Tiger, Lion, Horse or Eagle. The label should be adaptable to a product line of wines. For example the label could be used for a Cabernet wine, Merlot, Chardonnay or Pinot. A slight modification to the label design should be incorporated to allow for the different varietals. Front label design only. Can utilize photo image in design.
The label would be around 5.75" x 3.50".

Target Market(s)

25-35 year old wine buyers in the global market

Industry/Entity Type

Retail

Font styles to use
Sans Serif

Requirements
Must have
• Wine name based on design (designer suggest name)
Wine varietals
Vintage date
Additional wording area
Nice to have
• Rectangular label preferred Front label only.

```html
<!DOCTYPE html>
<html lang="en">
<head>
<meta charset="utf-8">
<title>Amber Mane – Varietal Label Range</title>
<link href="https://fonts.googleapis.com/css2?family=Cinzel:wght@400;700&display=swap" rel="stylesheet">
<style>
  :root {
    --page: #ffffff;
    --charcoal: #161514;
    --charcoal-soft: #2a2724;
    --gold: #b8895a;
    --gold-light: #d9ad7c;
    --gold-dark: #6e4c2e;
    --ring: rgba(184, 137, 90, 0.45);
    --kraft: #c4a271;
    --kraft-light: #d6b98c;
    --ink: #2a2016;
    --cabernet: #5a1a78;
    --malbec: #f0611e;
    --merlot: #2f9c2a;
    --band-text: #ffffff;
  }
  * { box-sizing: border-box; margin: 0; padding: 0; }
  html, body {
    width: 1200px; height: 663px; overflow: hidden;
    background: var(--page);
  }
  .label-range {
    width: 1200px; height: 663px;
    display: flex; justify-content: center; align-items: center;
    gap: 44px;
  }
  .label {
    position: relative;
    width: 320px; height: 552px;
    box-shadow: 0 3px 10px rgba(0,0,0,0.28);
    overflow: hidden;
    font-family: "Cinzel", serif;
  }
  .label__panel {
    position: absolute; left: 0; top: 0;
    width: 320px; height: 448px;
    background: radial-gradient(ellipse at 50% 35%, var(--charcoal-soft) 0%, var(--charcoal) 75%);
  }
  .label__ridge {
    position: absolute; left: 0; top: 300px;
    width: 320px; height: 148px;
    background: linear-gradient(180deg, rgba(60,56,52,0) 0%, rgba(60,56,52,0.35) 45%, rgba(12,11,10,0.7) 100%);
  }
  .label__ring {
    position: absolute; left: 0; top: 0;
  }
  .label__lion-art {
    position: absolute; left: 60px; top: 62px;
    width: 200px; height: 200px;
    border-radius: 50%;
    background: radial-gradient(circle at 50% 45%, var(--gold-light) 0%, var(--gold) 50%, var(--gold-dark) 100%);
  }
  .label__name {
    position: absolute; left: 0; top: 318px; width: 320px;
    text-align: center;
    color: var(--gold);
    font-weight: 400;
    font-size: 32px; letter-spacing: 3px;
    line-height: 1;
  }
  .label__band {
    position: absolute; left: 0; top: 448px;
    width: 320px; height: 42px;
    display: flex; align-items: center; justify-content: center;
    color: var(--band-text);
    font-size: 16px; letter-spacing: 0.5px;
  }
  .label--cabernet .label__band { background: linear-gradient(90deg, var(--cabernet), #7a2a9a); }
  .label--malbec .label__band { background: linear-gradient(90deg, var(--malbec), #ff5a12); }
  .label--merlot .label__band { background: linear-gradient(90deg, var(--merlot), #3bb536); }
  .label__base {
    position: absolute; left: 0; top: 490px;
    width: 320px; height: 62px;
    background: radial-gradient(ellipse at 40% 40%, var(--kraft-light) 0%, var(--kraft) 75%);
    color: var(--ink);
    text-align: center;
  }
  .label__vintage {
    margin-top: 10px;
    font-weight: 700; font-size: 17px; letter-spacing: 1px;
    line-height: 1.2;
  }
  .label__abv {
    margin-top: 2px;
    font-size: 10px; letter-spacing: 0.5px;
  }
</style>
</head>
<body>
<main class="label-range">

  <article class="label label--cabernet">
    <div class="label__panel"></div>
    <div class="label__ridge" role="img" aria-label="Faint mountain ridge silhouette"></div>
    <svg class="label__ring" width="320" height="448" viewBox="0 0 320 448">
      <circle cx="160" cy="162" r="124" fill="none" stroke="#b8895a" stroke-opacity="0.45" stroke-width="1"/>
    </svg>
    <div class="label__lion-art" role="img" aria-label="Golden lion head illustration"></div>
    <h2 class="label__name">Amber Mane</h2>
    <div class="label__band">Cabernet Sauvignon</div>
    <div class="label__base">
      <p class="label__vintage">2020</p>
      <p class="label__abv">ALC 13% by vol</p>
    </div>
  </article>

  <article class="label label--malbec">
    <div class="label__panel"></div>
    <div class="label__ridge" role="img" aria-label="Faint mountain ridge silhouette"></div>
    <svg class="label__ring" width="320" height="448" viewBox="0 0 320 448">
      <circle cx="160" cy="162" r="124" fill="none" stroke="#b8895a" stroke-opacity="0.45" stroke-width="1"/>
    </svg>
    <div class="label__lion-art" role="img" aria-label="Golden lion head illustration"></div>
    <h2 class="label__name">Amber Mane</h2>
    <div class="label__band">Malbec</div>
    <div class="label__base">
      <p class="label__vintage">2020</p>
      <p class="label__abv">ALC 13% by vol</p>
    </div>
  </article>

  <article class="label label--merlot">
    <div class="label__panel"></div>
    <div class="label__ridge" role="img" aria-label="Faint mountain ridge silhouette"></div>
    <svg class="label__ring" width="320" height="448" viewBox="0 0 320 448">
      <circle cx="160" cy="162" r="124" fill="none" stroke="#b8895a" stroke-opacity="0.45" stroke-width="1"/>
    </svg>
    <div class="label__lion-art" role="img" aria-label="Golden lion head illustration"></div>
    <h2 class="label__name">Amber Mane</h2>
    <div class="label__band">Merlot</div>
    <div class="label__base">
      <p class="label__vintage">2020</p>
      <p class="label__abv">ALC 13% by vol</p>
    </div>
  </article>

</main>
</body>
</html>
```